presentation slide template in Adobe Indesign

Hi, we need to design a template for presentation slides as well as presentation-like documents in slide format. See our website: marlowvane-partners.example and also graphical profile attached as a file. I've also attached the images used on our web site.
Regards,
Anselm
Updates
Hi, a clarification: this is about a presentation template not a specific presentation based on the web site content. I only supplied the web site for you as a reference. I imagine the result would include a base slide template that can be used for the bulk of the slides in a presentation and then a number of template slides that can be inserted in to a presentation to make it visually more interesting.
Target Market(s)
Management Consulting, Financial Risk Advisory
Requirements
Must have
- End product must be an Adobe InDesign template.

```html
<!DOCTYPE html>
<html lang="en">
<head>
<meta charset="utf-8">
<title>Marlowvane Partners – Services Slide</title>
<link rel="stylesheet" href="https://fonts.googleapis.com/css2?family=Noto+Sans:wght@400;700&family=Tinos&display=swap">
<style>
  :root {
    --page: #ffffff;
    --ink: #1f1f1f;
    --muted: #8a8a8a;
    --rule: #a9a9ab;
    --accent: #0b7f9d;
    --photo-dark: #9c8f76;
    --photo-mid: #c9bea4;
    --photo-light: #e8e3d2;
    --veil: rgba(255, 255, 255, 0.86);
  }
  html, body {
    margin: 0;
    width: 1200px;
    height: 800px;
    overflow: hidden;
    background: var(--page);
  }
  .canvas {
    position: relative;
    width: 1200px;
    height: 800px;
    font-family: "Noto Sans", sans-serif;
    color: var(--ink);
  }
  .slide {
    position: absolute;
    left: 96px;
    top: 95px;
    width: 1008px;
    height: 612px;
    background: var(--page);
    box-shadow: 2px 4px 10px rgba(0, 0, 0, 0.35);
    overflow: hidden;
  }
  .slide__photo {
    position: absolute;
    left: 254px;
    top: 0;
    width: 754px;
    height: 612px;
    background:
      radial-gradient(ellipse at 75% 35%, var(--photo-light) 0%, transparent 60%),
      linear-gradient(160deg, var(--photo-dark) 0%, var(--photo-mid) 35%, var(--photo-light) 70%, var(--photo-mid) 100%);
  }
  .slide__content {
    position: absolute;
    left: 0;
    top: 73px;
    width: 504px;
    height: 480px;
    background: var(--page);
  }
  .slide__veil {
    position: absolute;
    left: 504px;
    top: 73px;
    width: 350px;
    height: 480px;
    background: var(--veil);
  }
  .rule {
    position: absolute;
    left: 42px;
    width: 812px;
    height: 6px;
    border-top: 2px solid var(--rule);
    border-bottom: 1px solid var(--rule);
    box-sizing: border-box;
  }
  .rule--top { top: 66px; }
  .rule--bottom { top: 554px; }
  .brand {
    position: absolute;
    left: 42px;
    top: 116px;
    margin: 0;
    font-family: "Tinos", serif;
    font-weight: 400;
    font-size: 31px;
    line-height: 34px;
    letter-spacing: 3px;
    color: var(--ink);
    text-transform: uppercase;
  }
  .section-title {
    position: absolute;
    left: 42px;
    top: 216px;
    margin: 0;
    font-family: "Tinos", serif;
    font-weight: 400;
    font-size: 22px;
    line-height: 28px;
    color: var(--ink);
  }
  .section-title__bar {
    position: absolute;
    left: 42px;
    top: 247px;
    width: 40px;
    height: 8px;
    background: var(--accent);
  }
  .body-copy {
    position: absolute;
    left: 43px;
    top: 280px;
    margin: 0;
    white-space: nowrap;
    font-size: 15.5px;
    line-height: 19.4px;
    letter-spacing: 0.1px;
    color: var(--ink);
  }
  .stats {
    position: absolute;
    left: 540px;
    top: 185px;
    width: 275px;
    height: 170px;
  }
  .stat-caption {
    font-family: "Noto Sans", sans-serif;
    font-size: 14px;
    fill: var(--muted);
  }
  .stat-value {
    font-family: "Noto Sans", sans-serif;
    font-weight: 700;
    font-size: 34px;
    fill: #2b2b2b;
  }
  .stat-unit {
    font-family: "Noto Sans", sans-serif;
    font-weight: 700;
    font-size: 10px;
    fill: #6a6a6a;
  }
  .side-copy {
    position: absolute;
    left: 541px;
    top: 404px;
    margin: 0;
    white-space: nowrap;
    font-size: 11.5px;
    line-height: 14.5px;
    color: var(--ink);
  }
  .site-url {
    position: absolute;
    left: 254px;
    top: 565px;
    width: 624px;
    margin: 0;
    text-align: center;
    font-family: "Noto Sans", sans-serif;
    font-weight: 700;
    font-size: 14px;
    letter-spacing: 2.6px;
    color: #ffffff;
  }
</style>
</head>
<body>
<div class="canvas">
  <section class="slide">
    <div class="slide__photo" role="img" aria-label="Warm sepia photograph of colourful kites and streamers on strings against a hazy sky"></div>
    <div class="slide__content"></div>
    <div class="slide__veil"></div>
    <div class="rule rule--top"></div>
    <div class="rule rule--bottom"></div>

    <p class="brand">Marlowvane<br>Partners</p>

    <h2 class="section-title">SERVICES</h2>
    <div class="section-title__bar"></div>

    <p class="body-copy">Lorem ipsum dolor sit amet, consectetur adipisic-<br>ing elit, sed do eiusmod tempor incididunt ut labore<br>et dolore magna aliqua. Ut enim ad minim veniam,<br>quis nostrud exercitation ullamco laboris nisi ut<br>aliquip ex ea commodo consequat. Duis aute irure<br>dolor in reprehenderit in voluptate velit esse cil-<br>lum dolore eu fugiat nulla pariatur. Excepteur sint<br>occaecat cupidatat non proident, sunt in culpa qui<br>officia deserunt mollit anim id est laborum.</p>

    <svg class="stats" viewBox="0 0 275 170" aria-label="Two progress rings: 73 percent Lorem Ipsum, 52 percent Dolor">
      <defs>
        <linearGradient id="ring-warm" gradientUnits="userSpaceOnUse" x1="100" y1="10" x2="20" y2="90">
          <stop offset="0" stop-color="#1aa6e0"/>
          <stop offset="0.45" stop-color="#7a4aa0"/>
          <stop offset="0.75" stop-color="#e0203a"/>
          <stop offset="1" stop-color="#f6b514"/>
        </linearGradient>
        <linearGradient id="ring-cool" gradientUnits="userSpaceOnUse" x1="0" y1="10" x2="0" y2="115">
          <stop offset="0" stop-color="#14b4ee"/>
          <stop offset="0.6" stop-color="#6a55a8"/>
          <stop offset="1" stop-color="#ee1c34"/>
        </linearGradient>
        <radialGradient id="disc-shade" cx="0.45" cy="0.4" r="0.6">
          <stop offset="0" stop-color="#ffffff"/>
          <stop offset="1" stop-color="#dedede"/>
        </radialGradient>
      </defs>
      <g class="stat">
        <ellipse cx="69" cy="128" rx="52" ry="4" fill="#000" opacity="0.06"/>
        <circle cx="69" cy="65" r="50" fill="none" stroke="#e4e4e4" stroke-width="10"/>
        <circle cx="69" cy="65" r="44" fill="url(#disc-shade)"/>
        <circle cx="69" cy="65" r="50" fill="none" stroke="url(#ring-warm)" stroke-width="10" stroke-dasharray="229.3 314.2" transform="rotate(-90 69 65)"/>
        <text class="stat-value" x="63" y="78" text-anchor="middle">73</text>
        <text class="stat-unit" x="88" y="60">%</text>
        <text class="stat-caption" x="69" y="155" text-anchor="middle">Lorem Ipsum</text>
      </g>
      <g class="stat">
        <ellipse cx="202" cy="128" rx="52" ry="4" fill="#000" opacity="0.06"/>
        <circle cx="202" cy="65" r="50" fill="none" stroke="#e4e4e4" stroke-width="10"/>
        <circle cx="202" cy="65" r="44" fill="url(#disc-shade)"/>
        <circle cx="202" cy="65" r="50" fill="none" stroke="url(#ring-cool)" stroke-width="10" stroke-dasharray="163.4 314.2" transform="rotate(-90 202 65)"/>
        <text class="stat-value" x="196" y="78" text-anchor="middle">52</text>
        <text class="stat-unit" x="221" y="60">%</text>
        <text class="stat-caption" x="202" y="155" text-anchor="middle">Dolor</text>
      </g>
    </svg>

    <p class="side-copy">Lorem ipsum dolor sit amet, consectetur<br>adipisicing elit, sed do eiusmod tempor inc-<br>ididunt ut labore et dolore magna aliqua.</p>

    <p class="site-url">marlowvane-partners.example</p>
  </section>
</div>
</body>
</html>
```